Automotive Repair Christmas Incentive Offer

We are an automotive repair shop that specializes in import auto repair. We need a postcard mailer that will target pre-existing customers for the Holiday season. On the front, we would like an image of a happy, female customer that is pointing to a message of holiday wishes with our company. The colors should be a traditional holiday theme with the predominant color being red. We would like the visual trail to start at the female's face and then travel to her finger pointing to the Happy Holidays message. On the reverse side, we would like to have the text read like the attached PDF file.

Target Market(s)

Females, 25-45, average household income $100000.00/year, college educated, kids in famile

Industry/Entity Type

Automotive

Font styles to use
Serif

Colors
ec1f27
9bcb3c
000000

Requirements
Must have
• Simple lines, clear and attractive font, be KRMB approved format for mailing, attractive images that are polished looking and high-quality, holiday colors
Should not have
• Cluttered images, hard to read font, complicated color schemes

```html
<!DOCTYPE html>
<html lang="en">
<head>
<meta charset="utf-8">
<title>Holiday Gift Postcard – Mailing Side</title>
<link rel="stylesheet" href="https://fonts.googleapis.com/css2?family=Berkshire+Swash&family=Barlow+Condensed:wght@500;600;700&display=swap">
<style>
  :root {
    --holiday-red: #ec1f27;
    --ink: #111111;
    --paper: #ffffff;
    --frost-light: #e6f3f8;
    --frost-mid: #cfe7f0;
    --rule: #3a3a3a;
    --gift-red: #c8202a;
    --gift-teal: #6f8d93;
    --snow: #f4f8fa;
  }
  * { margin: 0; padding: 0; box-sizing: border-box; }
  html, body { width: 1200px; height: 799px; overflow: hidden; background: var(--paper); }
  .postcard {
    position: relative;
    width: 1200px;
    height: 799px;
    overflow: hidden;
    background: var(--paper);
    font-family: "Barlow Condensed", "Arial Narrow", sans-serif;
    color: var(--ink);
  }
  .message-panel {
    position: absolute;
    left: 0; top: 0;
    width: 640px; height: 799px;
    background:
      radial-gradient(ellipse 420px 520px at 120px 360px, var(--frost-mid) 0%, rgba(207,231,240,0) 75%),
      linear-gradient(90deg, var(--frost-light) 0%, #eef7fa 45%, rgba(255,255,255,0) 100%);
  }
  .gift-artwork {
    position: absolute;
    left: 0; top: 460px;
    width: 330px; height: 339px;
    background:
      radial-gradient(ellipse 190px 110px at 110px 270px, var(--gift-red) 0%, rgba(200,32,42,0) 80%),
      radial-gradient(ellipse 150px 75px at 70px 150px, var(--gift-teal) 0%, rgba(111,141,147,0) 80%),
      radial-gradient(ellipse 120px 70px at 40px 50px, var(--gift-red) 0%, rgba(200,32,42,0) 80%),
      linear-gradient(180deg, rgba(244,248,250,0) 0%, var(--snow) 100%);
  }
  .headline {
    position: absolute;
    left: 42px; top: 18px;
    font-family: "Berkshire Swash", "Georgia", serif;
    font-size: 68px;
    font-style: italic;
    font-weight: 400;
    line-height: 84px;
    color: var(--holiday-red);
    text-shadow: 2px 2px 0 rgba(90,0,0,0.35);
    white-space: nowrap;
  }
  .greeting {
    position: absolute;
    left: 42px; top: 118px;
    width: 532px;
    font-size: 23px;
    font-weight: 500;
    line-height: 33px;
  }
  .offer {
    position: absolute;
    left: 42px; top: 308px;
    font-size: 23px;
    font-weight: 500;
    white-space: nowrap;
  }
  .offer-amount {
    font-size: 38px;
    font-weight: 600;
    color: var(--holiday-red);
  }
  .call-to-action {
    position: absolute;
    left: 42px; top: 378px;
    font-size: 24px;
    font-weight: 700;
    letter-spacing: 0.3px;
    white-space: nowrap;
  }
  .sign-off {
    position: absolute;
    right: 607px; top: 436px;
    text-align: right;
    font-size: 23px;
    font-weight: 500;
    line-height: 33px;
    white-space: nowrap;
  }
  .shop-details {
    position: absolute;
    left: 361px; top: 568px;
    font-size: 23px;
    font-style: normal;
    font-weight: 500;
    line-height: 34px;
    white-space: nowrap;
  }
  .shop-name {
    display: block;
    font-size: 36px;
    font-weight: 600;
    line-height: 44px;
    letter-spacing: 0;
    margin-bottom: 4px;
    color: var(--ink);
  }
  .divider {
    position: absolute;
    left: 621px; top: 56px;
    width: 1px; height: 688px;
    background: var(--rule);
  }
  .stamp-box {
    position: absolute;
    left: 1032px; top: 58px;
    width: 102px; height: 127px;
    border: 1.5px solid var(--rule);
  }
  .address-line {
    position: absolute;
    left: 689px;
    width: 445px;
    height: 1px;
    background: var(--rule);
  }
  .address-line--1 { top: 470px; }
  .address-line--2 { top: 534px; }
  .address-line--3 { top: 599px; }
  .address-line--4 { top: 662px; }
</style>
</head>
<body>
  <main class="postcard">
    <div class="message-panel"></div>
    <div class="gift-artwork" role="img" aria-label="Stack of wrapped red and teal holiday gift boxes with frosted pine branches in snow"></div>

    <h1 class="headline">Our Holiday Gift</h1>

    <p class="greeting">
      From our family to yours,<br>
      We, at BROOKFIELD AUTO, would like to give thanks for all of<br>
      your patronage and support over the past year.<br>
      In appreciation for letting us take care of your vehicle, we’d<br>
      like to give you a gift of
    </p>

    <p class="offer"><span class="offer-amount">$25.00 off</span> your next service.</p>

    <p class="call-to-action">CALL: 555-0142 FOR YOUR APPOINTMENT</p>

    <p class="sign-off">Sincerely,<br>The Brookfield Family</p>

    <address class="shop-details">
      <span class="shop-name">BROOKFIELD AUTO</span>
      2214 Alder Road<br>
      Kestrel, AK 99601<br>
      907-555-0142<br>
      brookfieldimportauto.com
    </address>

    <div class="divider"></div>
    <div class="stamp-box"></div>
    <div class="address-line address-line--1"></div>
    <div class="address-line address-line--2"></div>
    <div class="address-line address-line--3"></div>
    <div class="address-line address-line--4"></div>
  </main>
</body>
</html>
```